【依頼の目的/概要】
電子書籍(plumet)の表紙デザインをお願いします。

【画像サイズ】
表紙ファイルの理想的な寸法は2,560×1,600ピクセルです。

【タイトル】
あの窓辺にまた灯りがともる静かな暮らしの場を一から育てるための手引き

サブキャッチ
~住む人の歩みを一緒に編み直す語らい中心の新しい手法~

【著者】
株式会社MRTOV
代表取締役 江坂 なつえ

【本の内容】
誰もが迎える老いのステージを「自分の人生まんざらでもなかったなぁ」と思っていただける新手法ナラティブアプローチの方法を介護哲学と共に解説しています。

*本文を参考資料として添付します。

【デザイン要望】
特にイメージにこだわりはありませんので、自由な発想でのデザインご応募を楽しみにしています。
*次点、次次点の方への参加報酬を設定いたしました。
*その他、必要な情報がありましたらお問い合わせください。

暖かいイメージが伝わってきます。
一番人気でした。

この度は力作を多数ご提案いただき、有難うございました。
初めてワクトリアを利用させていただいたのですが、たくさんの洗練されたご提案があったこと、はるかに自分の予想を上回りました。
これからも、利用させていただきたいと思いますので、よろしくお願いいたします。

```html
<!DOCTYPE html>
<html lang="ja">
<head>
<meta charset="utf-8">
<title>あの窓辺にまた灯りがともる静かな暮らしの場を一から育てるための手引き</title>
<link rel="stylesheet" href="https://fonts.googleapis.com/css2?family=Noto+Serif+JP:wght@500;700;900&family=Noto+Sans+JP:wght@500;700&display=swap">
<style>
  :root {
    --paper: #ffffff;
    --ink: #1b1b1b;
    --accent-pink: #e8457f;
    --band-green: #9cc43e;
    --portrait-light: #f5f1ec;
    --portrait-tone: #c6e4ea;
    --garden-green: #5f8a3c;
    --garden-pink: #e9a3bd;
    --garden-sky: #cfe3ee;
  }
  html, body {
    margin: 0;
    padding: 0;
    width: 750px;
    height: 1200px;
    overflow: hidden;
    background: var(--paper);
  }
  .cover {
    position: relative;
    width: 750px;
    height: 1200px;
    overflow: hidden;
    background: var(--paper);
    font-family: "Noto Serif JP", serif;
    color: var(--ink);
  }
  .top-band {
    position: absolute;
    left: 0; top: 0;
    width: 750px; height: 26px;
    background: var(--band-green);
  }
  .portrait-photo {
    position: absolute;
    left: 220px; top: 410px;
    width: 360px; height: 420px;
    background:
      radial-gradient(ellipse at 50% 45%, var(--portrait-tone) 0%, rgba(198,228,234,0.5) 40%, rgba(255,255,255,0) 70%),
      linear-gradient(180deg, var(--portrait-light), var(--paper));
  }
  .garden-photo {
    position: absolute;
    left: 0; top: 828px;
    width: 750px; height: 372px;
    background: linear-gradient(180deg, var(--garden-sky) 0%, var(--garden-pink) 30%, var(--garden-green) 62%, #4a6a34 100%);
  }
  .book-title, .subtitle { margin: 0; font-size: inherit; font-weight: inherit; }
  .vcol {
    position: absolute;
    display: block;
    writing-mode: vertical-rl;
    white-space: nowrap;
    line-height: 1;
    margin: 0;
  }
  .title-lead {
    left: 632px; top: 34px;
    width: 84px; height: 790px;
    font-size: 78px;
    font-weight: 900;
  }
  .title-line {
    top: 64px;
    width: 62px; height: 480px;
    font-size: 46px;
    font-weight: 700;
  }
  .title-line--second { left: 532px; }
  .title-line--third { left: 458px; }
  .title-line--fourth { left: 384px; }
  .emphasis {
    text-emphasis: filled dot var(--accent-pink);
    -webkit-text-emphasis: filled dot var(--accent-pink);
    text-emphasis-position: over right;
    -webkit-text-emphasis-position: over right;
  }
  .subtitle-line {
    left: 314px; top: 300px;
    width: 48px; height: 470px;
    font-size: 30px;
    font-weight: 500;
  }
  .subtitle-accent {
    left: 228px; top: 170px;
    width: 64px; height: 620px;
    font-size: 50px;
    font-weight: 900;
    color: var(--accent-pink);
  }
  .author {
    position: absolute;
    right: 18px; bottom: 18px;
    text-align: right;
    font-family: "Noto Sans JP", sans-serif;
    color: var(--paper);
    line-height: 1.25;
  }
  .author-label { font-size: 24px; font-weight: 500; color: var(--accent-pink); }
  .author-company { font-size: 34px; font-weight: 700; }
  .author-name { font-size: 30px; font-weight: 700; }
</style>
</head>
<body>
  <main class="cover">
    <div class="top-band"></div>
    <div class="portrait-photo" role="img" aria-label="小さな家の模型を両手に持って微笑む年配の女性の写真"></div>
    <div class="garden-photo" role="img" aria-label="花の咲く庭のベンチで語らう年配の女性たちの写真"></div>

    <h1 class="book-title">
      <span class="vcol title-lead">あの窓辺にまた灯りが</span>
      <span class="vcol title-line title-line--second">ともる静かな暮らしの</span>
      <span class="vcol title-line title-line--third">場を一から育てる</span>
      <span class="vcol title-line title-line--fourth">ための<span class="emphasis">手引き</span></span>
    </h1>

    <div class="subtitle">
      <p class="vcol subtitle-line">~住む人の歩みを<span class="emphasis">一緒</span>に編み直す</p>
      <p class="vcol subtitle-accent">語らい中心の新しい手法~</p>
    </div>

    <div class="author">
      <div class="author-label">著者</div>
      <div class="author-company">株式会社MRTOV</div>
      <div class="author-name">代表取締役 江坂 なつえ</div>
    </div>
  </main>
</body>
</html>
```